Brand Business Card for Hotel Cloud Management System

Hello designers,
we are looking for a new brand business card for our product Stayvora. Our brand Stayvora is a hotel management system for small hotels, B&B, guesthouses etc. and just recently we are expanding our offer to other European markets. Therefore we need a business card that will communicate not only to the end-users (hoteliers) but also to potential business partners/ We would like the brand business card to be professional looking, but not too serius, modern, elegant, clean, Our brand color is orange, dark grey and it would be nice to see both combined.

Please visit our website www.stayvora.eu to get more impression on what our brand stayvora stands for.

Please find attached stayvora logo.

Target Market(s)

small hotels, hoteliers, B&B owners, potential business partners

Industry/Entity Type

Software Service

Contact Information for Business Card

Stayvora
- hotel software solutions - web booking engine - multi channel manager
www.stayvora.eu
T: +38614738265
E: info@stayvora.net

Font styles to use
Serif
Sans Serif

Colors
f37122
aaaaaa
606060
f6f6f6

Requirements
Must have
• Logo of the brand
• the layout of the business card should be in connection with the look and feel of the website stayvora.eu and logo stayvora;

```html
<!DOCTYPE html>
<html lang="en">
<head>
<meta charset="utf-8">
<title>Stayvora Business Card</title>
<link rel="stylesheet" href="https://fonts.googleapis.com/css2?family=Roboto:wght@400;500;700&family=Roboto+Condensed:wght@500&display=swap">
<style>
  :root {
    --orange: #f37122;
    --band-orange: #e96a22;
    --ink: #161616;
    --text-grey: #505050;
    --rule: #8a8a8a;
    --paper: #f4f4f4;
    --backdrop: #2b2b2b;
  }
  * { margin: 0; padding: 0; box-sizing: border-box; }
  html, body { width: 1200px; height: 960px; overflow: hidden; }
  body {
    background: var(--backdrop);
    font-family: "Roboto", Arial, sans-serif;
    position: relative;
  }
  .card {
    position: absolute;
    width: 600px;
    height: 343px;
    background: var(--paper);
    border-radius: 16px;
    overflow: hidden;
  }
  .card--front { left: 314px; top: 113px; }
  .card--back { left: 311px; top: 472px; }

  .brand { position: absolute; color: var(--ink); }
  .brand__name {
    display: flex;
    align-items: center;
    font-weight: 700;
    letter-spacing: -1px;
    line-height: 1;
    color: var(--ink);
  }
  .brand__dot {
    display: inline-block;
    background: var(--orange);
    border-radius: 50%;
  }
  .brand__tagline {
    font-weight: 400;
    color: var(--ink);
    line-height: 1;
  }

  .card--front .brand { right: 41px; top: 74px; text-align: left; }
  .card--front .brand__name { font-size: 44px; }
  .card--front .brand__dot { width: 12px; height: 12px; margin-left: 6px; }
  .card--front .brand__tagline { font-size: 15px; margin-top: 4px; }

  .person { position: absolute; left: 41px; top: 196px; }
  .person__name {
    font-family: "Roboto Condensed", "Arial Narrow", sans-serif;
    font-weight: 500;
    font-size: 23px;
    color: var(--orange);
    line-height: 1;
  }
  .person__role {
    font-size: 14px;
    font-weight: 500;
    color: var(--ink);
    margin-top: 4px;
  }
  .rule {
    position: absolute;
    left: 41px; right: 41px; top: 251px;
    height: 1px;
    background: var(--rule);
  }
  .contact {
    position: absolute;
    left: 41px; top: 263px;
    list-style: none;
    font-size: 14px;
    color: var(--text-grey);
  }
  .contact__item { display: flex; align-items: center; height: 19px; }
  .contact__icon { width: 13px; height: 13px; margin-right: 9px; }
  .website {
    position: absolute;
    right: 39px; top: 283px;
    font-size: 14px;
    color: var(--text-grey);
  }
  .front-band { position: absolute; left: 0; bottom: 0; width: 600px; height: 22px; }

  .card--back .brand { left: 151px; top: 136px; }
  .card--back .brand__name { font-size: 60px; }
  .card--back .brand__dot { width: 16px; height: 16px; margin-left: 8px; }
  .card--back .brand__tagline { font-size: 20px; margin-top: 4px; }

  .services {
    position: absolute;
    left: 0; right: 0; top: 288px;
    height: 27px;
    background: var(--ink);
    color: #ffffff;
    font-size: 15px;
    display: flex;
    justify-content: center;
    align-items: center;
    list-style: none;
  }
  .services__item { display: flex; align-items: center; }
  .services__item + .services__item::before {
    content: "";
    width: 7px; height: 7px;
    border-radius: 50%;
    background: var(--orange);
    margin: 0 3px;
  }
</style>
</head>
<body>
  <section class="card card--front">
    <div class="brand">
      <div class="brand__name">Stayvora<span class="brand__dot"></span></div>
      <div class="brand__tagline">hotel pms service</div>
    </div>

    <div class="person">
      <div class="person__name">MARKO LENART</div>
      <div class="person__role">CEO/FOUNDER</div>
    </div>

    <div class="rule"></div>

    <ul class="contact">
      <li class="contact__item">
        <svg class="contact__icon" viewBox="0 0 24 24" aria-hidden="true"><path fill="#f37122" d="M6.6 10.8a15.1 15.1 0 0 0 6.6 6.6l2.2-2.2a1 1 0 0 1 1-.25 11.4 11.4 0 0 0 3.6.57 1 1 0 0 1 1 1V20a1 1 0 0 1-1 1A17 17 0 0 1 3 4a1 1 0 0 1 1-1h3.5a1 1 0 0 1 1 1c0 1.25.2 2.45.57 3.57a1 1 0 0 1-.25 1z"/></svg>
        +38614738265
      </li>
      <li class="contact__item">
        <svg class="contact__icon" viewBox="0 0 24 24" aria-hidden="true"><path fill="#f37122" d="M2 5h20v14H2z"/><path fill="none" stroke="#f4f4f4" stroke-width="2" d="M2.5 5.5 12 13l9.5-7.5"/></svg>
        info@stayvora.net
      </li>
    </ul>

    <div class="website">www.stayvora.eu</div>

    <svg class="front-band" viewBox="0 0 600 22" aria-hidden="true">
      <polygon points="0,0 395,0 389,22 0,22" fill="#e96a22"/>
      <polygon points="399,0 600,0 600,22 393,22" fill="#161616"/>
    </svg>
  </section>

  <section class="card card--back">
    <div class="brand">
      <div class="brand__name">Stayvora<span class="brand__dot"></span></div>
      <div class="brand__tagline">hotel pms service</div>
    </div>

    <ul class="services">
      <li class="services__item">hotel software solutions</li>
      <li class="services__item">web booking engine</li>
      <li class="services__item">multi channel manager</li>
    </ul>
  </section>
</body>
</html>
```